Power Point Presentation to Large Audience

Make a consistent look and feel but also make it a compelling presentation. I have attached a summary of my presentation

Target Market(s)

I am making a presentation to investors. Need a consistent look feel but I need it to be simple in design

Requirements
Must have
• Use http://brightlane4jobs.example/ for any background into the company
Nice to have
• My presentation has to be short, less than 10 to 15 minutes. The format I have attached is my basic content, I need it cleaned up and put in a compelling format

```html
<!DOCTYPE html>
<html lang="en">
<head>
<meta charset="utf-8">
<title>Brightlane Jobs – Investor Deck Slides</title>
<link href="https://fonts.googleapis.com/css2?family=Open+Sans:ital,wght@0,400;0,600;0,700;1,400&display=swap" rel="stylesheet">
<style>
  :root {
    --orange: #f7861f;
    --orange-soft: #f9a54f;
    --slate: #6e7b7f;
    --slate-box: #7d8a8c;
    --ink: #4a4f52;
    --icon-light: #c9d0d1;
    --white: #ffffff;
    --page: #ffffff;
  }
  * { box-sizing: border-box; margin: 0; padding: 0; }
  html, body { width: 1200px; height: 523px; overflow: hidden; background: var(--page); }
  body { position: relative; font-family: "Open Sans", Arial, sans-serif; color: var(--ink); }

  .slide { position: absolute; overflow: hidden; background: var(--white); }
  .footer-note { position: absolute; font-size: 5px; color: var(--ink); white-space: nowrap; }
  .partner-badge { position: absolute; width: 20px; height: 8px; background: var(--orange); border-radius: 2px; }

  .brand { position: absolute; text-align: center; }
  .brand-name { font-weight: 600; color: var(--slate); line-height: 1.1; }
  .brand-tagline { font-weight: 400; color: var(--slate); line-height: 1.3; }

  /* Slide: quote */
  .slide-quote { left: 0; top: 0; width: 464px; height: 260px; }
  .slide-quote .brand { left: 30px; top: 138px; width: 200px; }
  .slide-quote .brand-name { font-size: 19px; }
  .slide-quote .brand-tagline { font-size: 9px; }
  .quote-photo { position: absolute; left: 272px; top: 0; width: 192px; height: 260px;
    background: radial-gradient(circle at 30% 35%, #fbb870 0%, var(--orange-soft) 45%, #f3953a 100%); }
  .quote-notch { position: absolute; left: 262px; top: 118px; }
  .quote-text { position: absolute; left: 290px; top: 74px; width: 146px; color: var(--white);
    font-size: 12.5px; line-height: 1.32; text-align: center; }
  .quote-mark { font-size: 30px; font-weight: 700; color: #fbd0a3; line-height: 0; vertical-align: -11px; }
  .quote-author { display: block; margin-top: 20px; font-size: 7px; }

  /* Slide: question */
  .slide-question { left: 0; top: 262px; width: 464px; height: 261px; background: var(--orange); }
  .question-circle { position: absolute; left: -8px; top: -50px; width: 480px; height: 480px; border-radius: 50%; background: var(--white); }
  .question-text { position: absolute; left: 88px; top: 52px; width: 300px; text-align: center;
    font-size: 31px; font-weight: 600; color: var(--slate); line-height: 44px; }

  /* Centre brand */
  .brand-center { left: 472px; top: 278px; width: 256px; }
  .brand-center .brand-name { font-size: 24px; }
  .brand-center .brand-tagline { font-size: 11px; }

  /* Slide: learning model */
  .slide-model { left: 736px; top: 0; width: 464px; height: 260px; }
  .model-art { position: absolute; left: 0; top: 0; width: 151px; height: 260px; background: var(--orange); }
  .model-title { position: absolute; left: 176px; top: 33px; font-size: 18px; font-weight: 700; color: var(--orange); white-space: nowrap; }
  .model-box { position: absolute; left: 218px; width: 189px; background: var(--slate-box); color: var(--white);
    font-size: 5.3px; line-height: 1.45; padding: 4px 6px 4px 40px; display: flex; align-items: center; }
  .model-box svg { position: absolute; left: 10px; top: 50%; transform: translateY(-50%); }
  .model-box em { font-style: italic; }

  /* Slide: where wrong */
  .slide-wrong { left: 736px; top: 262px; width: 464px; height: 261px; }
  .wrong-band { position: absolute; left: 6px; top: 20px; width: 320px; height: 32px; background: var(--orange);
    color: var(--white); font-size: 17.5px; font-weight: 400; padding: 3px 0 0 18px; white-space: nowrap; }
  .wrong-icon { position: absolute; top: 88px; }
  .wrong-copy { position: absolute; font-size: 8.8px; line-height: 1.38; color: var(--ink); width: 130px; }
</style>
</head>
<body>

  <section class="slide slide-quote">
    <div class="brand">
      <div class="brand-name">Brightlane Jobs</div>
      <div class="brand-tagline">Learning that leads somewhere</div>
    </div>
    <div class="quote-photo" role="img" aria-label="Soft-focus warm orange photograph behind the quote"></div>
    <svg class="quote-notch" width="12" height="30" viewBox="0 0 12 30"><polygon points="12,0 0,15 12,30" fill="#f9a54f"/></svg>
    <p class="quote-text"><span class="quote-mark">“</span> To find out what one is fitted to do, and to secure an opportunity to do it, is the key to happiness <span class="quote-mark">”</span><span class="quote-author">– Marion Tate</span></p>
    <div class="footer-note" style="left:6px; top:252px;">KV7ed™ BrightlaneJobs™ 2018 Trademark KV7ed, LLC</div>
    <div class="partner-badge" style="left:216px; top:248px;"></div>
  </section>

  <section class="slide slide-question">
    <div class="question-circle"></div>
    <h2 class="question-text">Has personalized learning has gotten it wrong?</h2>
  </section>

  <div class="brand brand-center">
    <div class="brand-name">Brightlane Jobs</div>
    <div class="brand-tagline">Learning that leads somewhere</div>
  </div>

  <section class="slide slide-model">
    <div class="model-art" role="img" aria-label="Light bulb illustration with the word learn"></div>
    <h2 class="model-title">Personalized Learning Model</h2>
    <div class="model-box" style="top:70px; height:34px;">
      <svg width="14" height="14" viewBox="0 0 14 14"><circle cx="7" cy="5" r="4" fill="none" stroke="#c9d0d1" stroke-width="1"/><rect x="5" y="10" width="4" height="2" fill="#c9d0d1"/></svg>
      Personalized Learning Model Definition:
    </div>
    <div class="model-box" style="top:110px; height:42px;">
      <svg width="14" height="14" viewBox="0 0 14 14"><circle cx="7" cy="7" r="6" fill="#c9d0d1"/></svg>
      <em>Personalized learning models seek to adapt the pace of learning and the instructional strategies being used to best fit each individual child's strengths, weaknesses, and interests.</em>
    </div>
    <div class="model-box" style="top:155px; height:35px;">
      <svg width="14" height="14" viewBox="0 0 14 14"><circle cx="7" cy="7" r="6" fill="none" stroke="#c9d0d1"/><circle cx="7" cy="7" r="3" fill="none" stroke="#c9d0d1"/><circle cx="7" cy="7" r="1" fill="#c9d0d1"/></svg>
      Personalized Learning Results:
    </div>
    <div class="model-box" style="top:196px; height:36px;">
      <svg width="14" height="14" viewBox="0 0 14 14"><rect x="1" y="2" width="12" height="3" fill="#c9d0d1"/><rect x="1" y="6" width="12" height="3" fill="#c9d0d1"/><rect x="1" y="10" width="12" height="3" fill="#c9d0d1"/></svg>
      “The evidence base is very weak at this point,” said Alan R. Hale, a senior scientist and the group's distinguished chair in education innovation.
    </div>
    <div class="footer-note" style="left:158px; top:252px;">KV7ed™ BrightlaneJobs™ 2018 Trademark KV7ed, LLC</div>
    <div class="partner-badge" style="left:436px; top:249px;"></div>
  </section>

  <section class="slide slide-wrong">
    <h2 class="wrong-band">Where has it Gone Wrong?</h2>
    <svg class="wrong-icon" style="left:64px;" width="40" height="40" viewBox="0 0 44 44">
      <circle cx="22" cy="22" r="22" fill="#f7861f"/>
      <path d="M17 30v-5a7 7 0 1 1 10 -2v7" fill="none" stroke="#fff" stroke-width="2.5" stroke-linecap="round"/>
      <circle cx="22" cy="18" r="2.5" fill="#fff"/>
    </svg>
    <svg class="wrong-icon" style="left:298px;" width="40" height="40" viewBox="0 0 44 44">
      <circle cx="22" cy="22" r="22" fill="#f7861f"/>
      <polyline points="14,22 20,28 31,16" fill="none" stroke="#fff" stroke-width="2.5" stroke-linecap="round" stroke-linejoin="round"/>
    </svg>
    <p class="wrong-copy" style="left:38px; top:148px;">Many versions of personalized learning seek to change or replace fundamental processes that shape the day to day life of schools—everything from how teachers prepare lessons to how students are graded.</p>
    <p class="wrong-copy" style="left:253px; top:154px;">HINT: We weren’t doing that well to begin with, replicating what doesn’t work into personalized learning plans doesn’t change behavior</p>
    <div class="footer-note" style="left:150px; top:248px;">KV7ed™ BrightlaneJobs™ 2018 Trademark KV7ed, LLC</div>
    <div class="partner-badge" style="left:414px; top:246px;"></div>
  </section>

</body>
</html>
```